Global software company seeking new website design

Our existing website no longer meets our needs. We are seeking to develop a new website in Wordpress and need the look/feel, navigation and graphics designed to best effect. An overview of our company, and a brief on the functionality/key messaging of the website is in the attached PDF

Industry/Entity Type

Software

```html
<!DOCTYPE html>
<html lang="en">
<head>
<meta charset="utf-8">
<title>Veltrano – Email Migration Software</title>
<link href="https://fonts.googleapis.com/css2?family=Open+Sans:wght@400;600;700&family=PT+Sans:wght@400;700&display=swap" rel="stylesheet">
<style>
:root{
  --ink:#333;
  --muted:#8a8a8a;
  --brand:#2f3f86;
  --blue:#4a74b8;
  --orange:#f5a623;
  --teal:#0f6b5e;
  --violet:#5b4ea3;
  --slate:#33576b;
  --dark:#1f1f1f;
  --darker:#161616;
  --line:#e3e3e3;
}
*{box-sizing:border-box;margin:0;padding:0}
html,body{width:731px;height:1200px;overflow:hidden;background:#fff}
body{position:relative;font-family:"Open Sans",Arial,sans-serif;color:var(--ink);font-size:6px}
.abs{position:absolute}
.display{font-family:"PT Sans",Arial,sans-serif}

/* header */
.site-header{left:0;top:0;width:731px;height:48px;background:#fff}
.logo{left:168px;top:17px;font-family:"PT Sans",Arial,sans-serif;font-weight:700;font-size:17px;color:var(--brand);display:flex;align-items:center;gap:5px}
.logo .mark{width:8px;height:8px;background:var(--orange)}
.main-nav{left:296px;top:28px;display:flex;gap:19px;font-size:5.5px;letter-spacing:.5px;color:var(--muted)}
.main-nav .active{color:var(--blue);font-weight:700}

/* hero */
.hero{left:0;top:48px;width:731px;height:180px;background:linear-gradient(#f3f4f6,#fafafb)}
.hero-art{left:216px;top:6px;width:300px;height:120px;border-radius:4px;background:linear-gradient(120deg,#e9eef3 0%,#dfe7d8 35%,#e6edf5 60%,#9ca2a8 100%)}
.hero-intro{left:168px;top:144px;width:280px;font-size:5.6px;line-height:1.6;color:#555}
.hero-intro b{color:var(--brand)}
.btn{height:15px;font-size:6px;color:#fff;font-weight:600;display:flex;align-items:center;justify-content:center;border-radius:2px}
.btn-demo{left:456px;top:144px;width:48px;background:var(--blue)}
.btn-quote{left:517px;top:144px;width:49px;background:var(--orange)}

/* features */
.features{left:168px;top:238px;width:398px;display:flex}
.feature{width:99.5px;text-align:center;padding:0 6px}
.feature svg{display:block;margin:0 auto 5px}
.feature h3{font-size:5.6px;font-weight:600;margin-bottom:4px}
.feature p{font-size:4.4px;color:var(--muted);line-height:1.5}

/* banner */
.banner{left:0;top:310px;width:731px;height:156px}
.banner-photo{left:0;top:0;width:731px;height:156px;background:linear-gradient(100deg,#5e8d94 0%,#9fbcc0 45%,#7e9da3 75%,#5f7e86 100%)}
.banner-kicker{left:0;top:26px;width:731px;text-align:center;color:#fff;font-size:6.4px;letter-spacing:.8px;font-weight:600}
.banner-title{left:0;top:50px;width:731px;text-align:center;color:#fff;font-size:23px;letter-spacing:.5px;font-weight:400}
.products{left:255px;top:93px;display:flex;gap:47px}
.product{width:60px;text-align:center;color:#fff;font-size:6px}
.product .badge{width:24px;height:24px;border-radius:4px;margin:0 auto 5px}

/* carousel */
.carousel{left:36px;top:466px;width:664px;height:80px;display:flex}
.tile{width:132.8px;height:80px}
.tile.t1{background:linear-gradient(#e8e8e8,#c9ccd0)}
.tile.t2{background:#3a3a3a;position:relative}
.tile.t3{background:linear-gradient(135deg,#7e8a96,#c1c8cf)}
.tile.t4{background:linear-gradient(135deg,#d8dde2,#8f9aa5)}
.tile.t5{background:linear-gradient(#e9e9e7,#bcbcb8)}
.tile-caption{position:absolute;left:0;top:16px;width:100%;text-align:center;color:#fff}
.tile-caption .dot{width:14px;height:14px;border-radius:50%;background:#e5e5e5;margin:0 auto 6px}
.tile-caption h4{font-size:8px;font-weight:400;letter-spacing:1px}
.tile-caption p{font-size:5.5px;color:var(--orange);margin-top:3px}
.arrow{top:496px;width:14px;height:20px;background:rgba(0,0,0,.45);display:flex;align-items:center;justify-content:center}

/* solutions */
.section-title{width:731px;left:0;text-align:center;font-family:"PT Sans",Arial,sans-serif;font-size:13px;color:#666}
.title-rule{top:583px;height:1px;background:var(--line);width:150px}
.solutions{left:168px;top:606px;display:flex;gap:4px}
.card{width:96.5px;height:94px;color:#fff;padding:10px 9px;position:relative}
.card h3{font-family:"PT Sans",Arial,sans-serif;font-size:10px;font-weight:400;margin-bottom:9px}
.card p{font-size:4.7px;line-height:1.7;font-weight:600}
.card .more{position:absolute;left:41px;bottom:9px;font-size:5px;display:flex;align-items:center;gap:5px}
.card .more i{width:8px;height:8px;border-radius:50%;background:#fff;display:block}
.card.blue{background:var(--blue)}
.card.orange{background:var(--orange)}
.card.teal{background:var(--teal)}
.card.violet{background:var(--violet)}

/* what we do */
.what{left:0;top:722px;width:731px;height:180px;background:var(--slate);color:#fff}
.what h2{position:absolute;left:0;top:28px;width:731px;text-align:center;font-family:"PT Sans",Arial,sans-serif;font-size:13px;font-weight:400}
.what-col{position:absolute;top:70px;width:200px;font-size:5.2px;line-height:1.5}
.what-col strong{font-family:"PT Sans",Arial,sans-serif;font-size:8px;font-weight:400}
.what-col .note{color:#9fb5c2;margin-top:4px;font-size:4.6px}
.what-art1{left:186px;top:108px;width:124px;height:72px;background:linear-gradient(#222,#444);border-radius:3px 3px 0 0}
.what-art2{left:395px;top:118px;width:150px;height:62px;background:linear-gradient(90deg,#c9d2d8,#e6c79a);border-radius:30px 30px 0 0}

/* most watched */
.watched-title{left:254px;top:924px;font-family:"PT Sans",Arial,sans-serif;font-size:13px;color:#777}
.watched-copy{left:175px;top:958px;width:162px;text-align:right;font-size:5.6px;line-height:1.75;color:#777}
.view-all{left:281px;top:1018px;width:56px;height:19px;border:1px solid #ccc;font-size:6px;color:#666;display:flex;align-items:center;justify-content:center;gap:5px}
.video{left:371px;top:928px;width:195px;height:110px;background:#111;padding:6px}
.video-frame{width:183px;height:85px;background:linear-gradient(135deg,#e7ecd7,#b9c88c 55%,#667a3f)}
.video-bar{display:flex;align-items:center;gap:6px;margin-top:5px;color:#ccc}
.video-bar .track{flex:1;height:3px;background:#444}

/* footer */
.site-footer{left:0;top:1056px;width:731px;height:126px;background:var(--dark);color:#aaa}
.footer-logo{left:186px;top:24px;font-family:"PT Sans",Arial,sans-serif;font-weight:700;font-size:15px;color:#8896c9;display:flex;align-items:center;gap:5px}
.footer-logo .mark{width:7px;height:7px;background:var(--orange)}
.footer-about{left:172px;top:60px;width:110px;text-align:center;font-size:4.5px;line-height:1.7;color:#888}
.footer-col{top:24px;font-size:4.6px;color:#999}
.footer-col h4{font-size:6px;color:#ddd;font-weight:600;letter-spacing:.4px;margin-bottom:10px}
.footer-col li{list-style:none;margin-bottom:8px}
.contact li{display:flex;align-items:center;gap:6px;margin-bottom:4px}
.contact li i{width:5px;height:5px;background:#888;border-radius:50%;display:block}
.socials{display:flex;gap:3px}
.socials span{width:10px;height:10px;border-radius:50%;background:#5873b8;display:block}
.bottom-bar{left:0;top:1182px;width:731px;height:18px;background:var(--darker);color:#777;font-size:4.4px}
.bottom-bar .copy{position:absolute;left:168px;top:7px}
.bottom-bar .links{position:absolute;left:421px;top:7px;letter-spacing:.3px}
</style>
</head>
<body>

<header class="site-header abs">
  <div class="logo abs">Veltrano <span class="mark"></span></div>
  <nav class="main-nav abs">
    <span class="active">SOLUTIONS</span><span>PRODUCTS</span><span>RESOURCES</span><span>PARTNERS</span><span>SUPPORT</span><span>COMPANY</span><span>BLOG</span>
    <svg width="6" height="6" viewBox="0 0 6 6"><circle cx="2.5" cy="2.5" r="1.8" fill="none" stroke="#888" stroke-width=".8"/><path d="M3.8 3.8L5.6 5.6" stroke="#888" stroke-width=".8"/></svg>
  </nav>
</header>

<section class="hero abs">
  <div class="hero-art abs" role="img" aria-label="Illustration of colourful email envelopes flowing through a migrator into a steel safe"></div>
  <p class="hero-intro abs"><b>Veltrano</b> provides scalable, trusted, automated and rapid solutions for the migration of email and user data between email archives, <b>MailCore Server, CloudDesk and PST files.</b></p>
  <div class="btn btn-demo abs">Request Demo</div>
  <div class="btn btn-quote abs">Get a Quote</div>
</section>

<section class="features abs">
  <div class="feature">
    <svg width="12" height="10" viewBox="0 0 12 10"><rect x="1" y="1" width="10" height="6.5" fill="none" stroke="#333" stroke-width="1"/><path d="M4 9.5h4M6 7.5v2" stroke="#333"/></svg>
    <h3>Cloud, Mobile &amp; Virtualization</h3>
    <p>Legacy on-premise email, file and archiving systems are a barrier to the opportunities presented by cloud and mobile</p>
  </div>
  <div class="feature">
    <svg width="10" height="10" viewBox="0 0 10 10"><rect x="2.5" y="2.5" width="5" height="5" fill="#333"/><path d="M1 3.5h1.5M1 6.5h1.5M7.5 3.5H9M7.5 6.5H9M3.5 1v1.5M6.5 1v1.5M3.5 7.5V9M6.5 7.5V9" stroke="#333"/></svg>
    <h3>Flexibility, Value &amp; Opportunity</h3>
    <p>IT budgets are being squeezed and users are demanding more. Cloud, storage and BYOD initiatives are delayed by legacy</p>
  </div>
  <div class="feature">
    <svg width="10" height="10" viewBox="0 0 10 10"><path d="M1 5L9 1L6 9L5 6Z" fill="none" stroke="#333" stroke-width=".9"/></svg>
    <h3>Control, Speed &amp; Risk</h3>
    <p>Veltrano has the proven products and methods to manage, automate and audit the migration of email archives</p>
  </div>
  <div class="feature">
    <svg width="10" height="10" viewBox="0 0 10 10"><circle cx="5" cy="5.6" r="3.6" fill="none" stroke="#333"/><path d="M5 3.5v2.3M4 1h2" stroke="#333"/></svg>
    <h3>Because CHANGE is our Business</h3>
    <p>We fully understand the business demands of our customers and enterprise migration</p>
  </div>
</section>

<section class="banner abs">
  <div class="banner-photo abs" role="img" aria-label="Photo of a hand touching a tablet screen"></div>
  <p class="banner-kicker abs">WE WORK HARD TO GIVE YOU</p>
  <h2 class="banner-title abs">A UNIQUE EXERIENCE</h2>
  <div class="products abs">
    <div class="product"><div class="badge" style="background:#f0b416"></div>VaultRelay</div>
    <div class="product"><div class="badge" style="background:#4cae3c"></div>BoxRelay</div>
    <div class="product"><div class="badge" style="background:#3d7fc4"></div>FileDeck</div>
  </div>
</section>

<section class="carousel abs">
  <div class="tile t1" role="img" aria-label="Photo of a calculator on financial charts"></div>
  <div class="tile t2">
    <div class="tile-caption"><div class="dot"></div><h4>PROJECT TITLE</h4><p>Lorem Ipsum is simply dummy text</p></div>
  </div>
  <div class="tile t3" role="img" aria-label="Photo of payment cards"></div>
  <div class="tile t4" role="img" aria-label="Photo of a watch on a world map"></div>
  <div class="tile t5" role="img" aria-label="Photo of rolled blueprints"></div>
</section>
<div class="arrow abs" style="left:36px"><svg width="5" height="8" viewBox="0 0 5 8"><path d="M4 1L1 4l3 3" fill="none" stroke="#fff" stroke-width="1.2"/></svg></div>
<div class="arrow abs" style="left:686px"><svg width="5" height="8" viewBox="0 0 5 8"><path d="M1 1l3 3-3 3" fill="none" stroke="#fff" stroke-width="1.2"/></svg></div>

<div class="title-rule abs" style="left:168px"></div>
<div class="title-rule abs" style="left:416px"></div>
<h2 class="section-title abs" style="top:575px">Our Solutions</h2>

<section class="solutions abs">
  <article class="card blue"><h3>Scalable</h3><p>Lorem Ipsum is simply dummy text of the printing and typesetting industry. Lorem Ipsum has been</p><span class="more"><i></i>Read More</span></article>
  <article class="card orange"><h3>Trusted</h3><p>Lorem Ipsum is simply dummy text of the printing and typesetting industry. Lorem Ipsum has been the industry's</p><span class="more"><i></i>Read More</span></article>
  <article class="card teal"><h3>Automated</h3><p>Lorem Ipsum is simply dummy text of the printing and typesetting industry. Lorem Ipsum has been the industry's standard dummy text ever since</p><span class="more"><i></i>Read More</span></article>
  <article class="card violet"><h3>Rapid</h3><p>Lorem Ipsum is simply dummy text of the printing and typesetting industry. Lorem Ipsum has been</p><span class="more"><i></i>Read More</span></article>
</section>

<section class="what abs">
  <h2>What We Do</h2>
  <div class="what-col" style="left:168px"><strong>Technical</strong> – Software that powers migration of email archives, MailCore and PST files.<p class="note">Lorem Ipsum is simply dummy text of the printing and typesetting</p></div>
  <div class="what-col" style="left:395px;width:175px"><strong>Business</strong> – Software that drive down the cost of email migration and delivers projects on time and on budget.<p class="note">Lorem Ipsum is simply dummy text of the printing</p></div>
  <div class="what-art1 abs" role="img" aria-label="Illustration of a laptop showing a product graphic"></div>
  <div class="what-art2 abs" role="img" aria-label="Illustration of email icons circling a computer screen"></div>
</section>

<h2 class="watched-title abs">Most Watched</h2>
<p class="watched-copy abs">Lorem Ipsum is simply dummy text of the printing and typesetting industry. Lorem Ipsum has been the industry's standard dummy text ever since the 1500s, when an unknown printer took a galley of type and scrambled it to make a type specimen book</p>
<div class="view-all abs"><svg width="6" height="5" viewBox="0 0 6 5"><path d="M0 .5h6M0 2.5h6M0 4.5h6" stroke="#666" stroke-width=".8"/></svg>View All</div>
<div class="video abs">
  <div class="video-frame" role="img" aria-label="Video still of a laptop on a desk with a plant"></div>
  <div class="video-bar"><svg width="6" height="6" viewBox="0 0 6 6"><path d="M1 0.5L5.5 3 1 5.5z" fill="#ddd"/></svg><div class="track"></div><span style="font-size:5px">HD</span></div>
</div>

<footer class="site-footer abs">
  <div class="footer-logo abs">Veltrano <span class="mark"></span></div>
  <p class="footer-about abs">Lorem Ipsum is simply dummy text of the printing and typesetting industry. Lorem Ipsum has been the industry's standard dummy text ever since.</p>
  <div class="footer-col abs" style="left:309px">
    <h4>RECENT POST</h4>
    <ul><li>Lorem Ipsum is simply dummy text</li><li>Lorem Ipsum is simply dummy text</li><li>Lorem Ipsum is simply dummy text</li><li>Lorem Ipsum is simply dummy text</li></ul>
  </div>
  <div class="footer-col contact abs" style="left:410px">
    <h4>CONTACT INFO</h4>
    <p style="margin-bottom:8px">Veltrano Ltd</p>
    <ul><li><i></i>4521 Green Row, City State 1234</li><li><i></i>123 456 78900</li><li><i></i>123 456 78900</li><li><i></i>info@veltrano.example</li><li><i></i>www.veltrano.example</li></ul>
  </div>
  <div class="footer-col abs" style="left:509px">
    <h4>SOCIAL LINKS</h4>
    <div class="socials"><span></span><span></span><span></span><span></span></div>
  </div>
</footer>
<div class="bottom-bar abs">
  <span class="copy">Copyright © 2014 Veltrano Ltd · All rights reserved</span>
  <span class="links">SOLUTION | PRODUCTS | RESOURCES | PARTNERS | SUPPORT | COMPANY | BLOG</span>
</div>

</body>
</html>
```